Flyer für Selbstwert-Coachin und Bewusstseinstrainerin
Der Flyer ist wunderschön, kreativ und edel geworden und wurde von der Designerin genau nach meinen Wünschen super umgesetzt! Ich bin sehr zufrieden und kann die Designerin Lenka4829 jedem nur empfehlen. Einfach Top!!! 1 A!!! Vielen herzlichen Dank!
Zielgruppe
Ich bin Selbstwert Coach und Bewusstseinstrainerin und möchte einen Flyer für mein neues Angebot 'Lichtweg Akademie für Jugendliche ab 16' gestalten lassen.
Die Zielgruppe sind Eltern von Jugendlichen in der Oberstufe, deren Kinder unter Schulstress und Leistungsdruck leiden und zu wenig Selbstbewusstsein haben.
Aufgabenstellung
Ich habe bereits das Titelbild bei Pixwald gesucht #731048259, bitte dieses nehmen, es kann auch ein ähnliches noch besseres vorgeschlagen werden.
Ich möchte einen ansprechenden, schönen, hochwertigen Flyer mit den Farben der Landingpage, gelb, blau, gold... und Bilder von Jugendlichen, dort wo Platz ist, ansprechend und klar. Bitte keine Schnörkel und 08 15 Figuren, das Auge soll hängen bleiben, der Flyer hängt straßenseitig. Dieser soll ein 6-seitiger Wickelfalz sein.

```html
<!DOCTYPE html>
<html lang="de">
<head>
<meta charset="utf-8">
<title>Lichtweg Akademie – Flyer</title>
<link href="https://fonts.googleapis.com/css2?family=Oswald:wght@500;600;700&family=Open+Sans:wght@400;600;700&display=swap" rel="stylesheet">
<style>
  :root {
    --navy: #262a5e;
    --violet: #3b3569;
    --yellow: #f6b90f;
    --gold: #b99a5a;
    --ink: #3a3a44;
    --paper: #ffffff;
    --backdrop: #dcdcdc;
    --rule: #d6d6dc;
  }
  * { box-sizing: border-box; margin: 0; padding: 0; }
  html, body { width: 1200px; height: 960px; overflow: hidden; }
  body {
    background: var(--backdrop);
    font-family: "Open Sans", sans-serif;
    color: var(--ink);
    position: relative;
  }
  .flyer {
    position: absolute;
    left: 50px; top: 91px;
    width: 1100px; height: 778px;
    background: var(--paper);
    display: flex;
    box-shadow: 0 10px 30px rgba(0,0,0,.18);
  }
  .panel { position: relative; width: 366.66px; height: 100%; overflow: hidden; }
  .panel + .panel { border-left: 1px solid var(--rule); }

  .photo { position: absolute; left: 0; top: 0; width: 100%; }
  .heading {
    font-family: "Oswald", sans-serif;
    font-weight: 700;
    text-transform: uppercase;
    color: var(--navy);
    line-height: 1.05;
  }

  /* Panel 1 – Vorteile */
  .panel-benefits .edge {
    position: absolute; left: 0; top: 230px; bottom: 0; width: 10px; background: var(--violet);
  }
  .photo-hands {
    height: 230px;
    background: linear-gradient(135deg, #eef3f7 0%, #d5e3ec 45%, #c9b9a4 100%);
  }
  .benefits { position: absolute; left: 34px; right: 26px; top: 252px; }
  .benefits .heading { font-size: 27px; margin-bottom: 12px; }
  .benefit-list { list-style: none; }
  .benefit-list li {
    position: relative; padding-left: 20px;
    font-size: 11.5px; line-height: 1.45; margin-bottom: 6px;
  }
  .benefit-list svg { position: absolute; left: 0; top: 3px; width: 12px; height: 12px; }
  .requirements { position: absolute; left: 34px; right: 26px; top: 560px; }
  .requirements .heading { font-size: 22px; margin-bottom: 10px; }
  .requirements p { font-size: 11.5px; line-height: 1.5; }

  /* Panel 2 – Kontakt */
  .photo-coach {
    height: 340px;
    background: linear-gradient(160deg, #4f6b3a 0%, #7d8f54 40%, #d8b27a 75%, #c89a68 100%);
  }
  .shapes { position: absolute; left: 0; top: 0; width: 100%; height: 100%; }
  .contact { position: absolute; left: 30px; right: 24px; top: 440px; }
  .contact .heading { font-size: 34px; margin-bottom: 16px; }
  .contact-name { font-family: "Oswald", sans-serif; font-weight: 600; font-size: 19px; color: var(--navy); }
  .contact-role { font-size: 11.5px; margin-bottom: 14px; }
  .contact-line { font-size: 11.5px; line-height: 1.6; }
  .contact-line b { color: var(--navy); display: inline-block; width: 52px; }
  .brand {
    position: absolute; left: 30px; bottom: 44px;
    display: flex; align-items: center; gap: 12px;
  }
  .brand-dot { width: 14px; height: 14px; border-radius: 50%; background: var(--gold); }
  .brand-name { font-family: "Open Sans", sans-serif; font-weight: 600; font-size: 19px; color: var(--gold); }

  /* Panel 3 – Titel */
  .photo-teen {
    height: 360px;
    background: linear-gradient(150deg, #c9c2b2 0%, #b59a7c 40%, #7c9bc4 85%, #6f8fbf 100%);
  }
  .title-label {
    position: absolute; right: 0; top: 58px;
    background: var(--yellow);
    padding: 10px 18px 10px 20px;
  }
  .title-label .heading { font-size: 26px; color: var(--navy); }
  .title-label small {
    font-family: "Open Sans", sans-serif; font-weight: 400;
    text-transform: none; font-size: 12px; color: var(--navy);
  }
  .pitch { position: absolute; left: 28px; width: 222px; top: 430px; }
  .pitch p { font-size: 13px; line-height: 1.5; margin-bottom: 10px; }
  .pitch .lead { font-weight: 600; color: var(--navy); }
  .cover-band {
    position: absolute; left: 0; right: 0; bottom: 0; height: 110px;
    background: var(--violet);
    color: #e4e2f2;
    padding: 24px 28px;
    font-size: 14px; line-height: 1.45;
  }
</style>
</head>
<body>
  <main class="flyer">
    <section class="panel panel-benefits">
      <div class="photo photo-hands" role="img" aria-label="Foto: Hand legt Holzwürfel mit Gesundheitssymbolen"></div>
      <div class="edge"></div>
      <div class="benefits">
        <h2 class="heading">Vorteile und Nutzen</h2>
        <ul class="benefit-list">
          <li><svg viewBox="0 0 12 12"><path d="M1 6.5 4.5 10 11 2" fill="none" stroke="#262a5e" stroke-width="2"/></svg>Beste Prävention für die psychische Gesundheit, Steigerung des Wohlbefindens von Geist, Körper und Seele</li>
          <li><svg viewBox="0 0 12 12"><path d="M1 6.5 4.5 10 11 2" fill="none" stroke="#262a5e" stroke-width="2"/></svg>Konkrete Lösungsansätze bei auftretenden Konflikten, Schulproblemen und Mobbing</li>
          <li><svg viewBox="0 0 12 12"><path d="M1 6.5 4.5 10 11 2" fill="none" stroke="#262a5e" stroke-width="2"/></svg>Veränderter Umgang bzw. Reduktion von Überforderung, Leistungsdruck und Schulstress</li>
          <li><svg viewBox="0 0 12 12"><path d="M1 6.5 4.5 10 11 2" fill="none" stroke="#262a5e" stroke-width="2"/></svg>Persönlichkeitsentwicklung, Lernen fürs Leben</li>
          <li><svg viewBox="0 0 12 12"><path d="M1 6.5 4.5 10 11 2" fill="none" stroke="#262a5e" stroke-width="2"/></svg>Grundlagen zur Gestaltung eines glücklichen, erfolgreichen Lebens</li>
          <li><svg viewBox="0 0 12 12"><path d="M1 6.5 4.5 10 11 2" fill="none" stroke="#262a5e" stroke-width="2"/></svg>Stärkung von Selbstbewusstsein, Selbstvertrauen, Selbstliebe und Selbstwert</li>
        </ul>
      </div>
      <div class="requirements">
        <h2 class="heading">Voraussetzungen für<br>die Teilnahme</h2>
        <p>Das wichtigste ist, dass dein Kind am Lehrgang teilnehmen will. Interesse, Neugierde und vor allem die Bereitschaft zur aktiven Umsetzung der Inhalte sind notwendig, um gute Ergebnisse zu erzielen.</p>
      </div>
    </section>

    <section class="panel panel-contact">
      <div class="photo photo-coach" role="img" aria-label="Porträtfoto der Veranstalterin im Grünen"></div>
      <svg class="shapes" viewBox="0 0 366 778" preserveAspectRatio="none" aria-hidden="true">
        <polygon points="0,250 120,340 0,340" fill="#f6b90f"/>
        <polygon points="190,340 366,340 366,500" fill="#3b3569"/>
      </svg>
      <div class="contact">
        <h2 class="heading">Kontakt &amp;<br>Veranstalterin:</h2>
        <p class="contact-name">Mag. Verena Lindtaler</p>
        <p class="contact-role">Selbstwert Coach, Bewusstseinstrainerin</p>
        <p class="contact-line"><b>E-Mail :</b>info@lichtweg-coaching.at</p>
        <p class="contact-line"><b>Mobil :</b>+43(0)660 412 5873</p>
      </div>
      <div class="brand">
        <span class="brand-dot"></span>
        <span class="brand-name">Verena Lindtaler</span>
      </div>
    </section>

    <section class="panel panel-cover">
      <div class="photo photo-teen" role="img" aria-label="Foto: jubelnde Jugendliche mit Locken"></div>
      <svg class="shapes" viewBox="0 0 366 778" preserveAspectRatio="none" aria-hidden="true">
        <polygon points="0,260 150,360 0,360" fill="#f6b90f"/>
        <polygon points="210,360 366,360 366,560" fill="#3b3569"/>
      </svg>
      <div class="title-label">
        <h1 class="heading">Lichtweg<br>Akademie <small>für Jugendliche ab 16</small></h1>
      </div>
      <div class="pitch">
        <p class="lead">Schulbegleitender Praxis Lehrgang für mentale Stärke und Selbstbewusstsein</p>
        <p>Schulstress &amp; Leistungsdruck bewältigen<br>Selbstsicherer, gelassener &amp; angstfrei werden</p>
        <p>und dabei ein starkes Selbstwertgefühl aufbauen und sich selbst vertrauen</p>
      </div>
      <div class="cover-band">Einfache Übungen, Techniken und Methoden für den Alltag und ein glückliches erfolgreiches Leben</div>
    </section>
  </main>
</body>
</html>
```